Business cards & stationery for a mortgage brokerage
Pebblewick Mortgages
Modern
Owen Drisdale
Director
17-19 Marsh Lane
Fernby Hollow
LT4 7QW
owen@pebblewickmortgages.co.uk
www.pebblewickmortgages.co.uk
Is it also possible to have this in an editable format? We will be using the design for a number of employees so we need to change some personal details
use your initiative on this please, but we would like it bright and colourful

```html
<!DOCTYPE html>
<html lang="en">
<head>
<meta charset="utf-8">
<title>Pebblewick Mortgages – Stationery</title>
<link rel="stylesheet" href="https://fonts.googleapis.com/css2?family=Open+Sans:wght@400;600;700&display=swap">
<style>
  :root{
    --bg:#e6e7e8;
    --paper:#ffffff;
    --green:#3d8b22;
    --green-dark:#2a6a17;
    --green-light:#8cc63f;
    --lime:#b7cc2c;
    --lime-light:#d6e05a;
    --ink:#4a4a4a;
    --rule:#cfcfcf;
    --faint:#eef3e8;
  }
  *{box-sizing:border-box;margin:0;padding:0}
  html,body{width:1200px;height:653px;overflow:hidden}
  body{background:var(--bg);font-family:"Open Sans",Arial,sans-serif;color:var(--ink);position:relative}
  .piece{position:absolute;background:var(--paper);box-shadow:0 1px 4px rgba(0,0,0,.25)}
  .caption{position:absolute;font-size:6px;font-weight:700;color:#555;text-align:center}

  .brand{display:flex;align-items:center;gap:4px}
  .brand-dot{border-radius:50%;background:var(--green);flex:none}
  .brand-name{font-weight:700;color:var(--green);white-space:nowrap}
  .tagline{color:#777;white-space:nowrap}

  /* business cards */
  .card{width:98px;height:60px;top:32px}
  .card-front{left:57px;padding:7px}
  .card-front .brand-dot{width:9px;height:9px}
  .card-front .brand-name{font-size:7.5px}
  .card-front .tagline{font-size:3px;margin:1px 0 0 13px}
  .card-front .person{position:absolute;left:7px;top:30px;font-size:3.6px;line-height:1.35}
  .card-front .person b{color:var(--green);font-size:4.2px}
  .card-front .contact{position:absolute;right:6px;top:30px;font-size:3.2px;line-height:1.45;text-align:right}
  .card-front .stripe{position:absolute;left:0;right:0;bottom:0;height:3px;background:var(--green)}
  .card-back{display:flex;align-items:center;justify-content:center}
  .card-back-1{left:165px}
  .card-back-1 .brand-dot{width:22px;height:22px}
  .card-back-2{left:275px;background:radial-gradient(circle at 30% 40%,var(--green-light),var(--green-dark))}
  .card-back-3{left:378px;background:radial-gradient(circle at 30% 40%,var(--lime-light),var(--lime) 55%,var(--green))}
  .card-back-2 .brand,.card-back-3 .brand{gap:4px}
  .card-back-2 .brand-dot,.card-back-3 .brand-dot{width:12px;height:12px;background:#fff}
  .card-back-2 .brand-name,.card-back-3 .brand-name{color:#fff;font-size:7px}

  /* letter-size sheets */
  .sheet{top:97px;width:305px;height:500px;padding:14px 16px}
  .sheet .brand-dot{width:14px;height:14px}
  .sheet .brand-name{font-size:11.5px}
  .sheet .tagline{font-size:3.6px;margin:1px 0 0 18px}
  .sheet .address{position:absolute;right:16px;top:14px;font-size:3.6px;line-height:1.5;width:95px;display:grid;grid-template-columns:1fr 1fr;gap:0 6px}
  .sheet .watermark{position:absolute;left:50%;top:52%;width:170px;height:170px;margin:-85px 0 0 -85px;border-radius:50%;background:var(--faint)}
  .sheet .footer-rule{position:absolute;left:0;right:0;bottom:8px;height:2px;background:var(--green)}
  .sheet .footer-rule::after{content:"";position:absolute;right:0;top:0;width:40%;height:2px;background:var(--lime)}
  .fax{left:8px}
  .letterhead{left:330px}
  .fax-title{position:absolute;right:16px;top:50px;font-size:7px;font-weight:700;color:var(--green)}
  .fax-form{position:absolute;left:16px;right:16px;top:60px;border-collapse:collapse;font-size:4px;z-index:1;background:#fff}
  .fax-form td{border:0.6px solid var(--rule);height:12px;padding:0 3px}
  .fax-form .label{width:26px;color:#666;background:#f7f7f7}
  .fax-checks{position:absolute;left:16px;right:16px;top:122px;display:flex;justify-content:space-between;font-size:4px;z-index:1}
  .fax-checks span::before{content:"";display:inline-block;width:4px;height:4px;border:0.6px solid #888;margin-right:2px;vertical-align:-0.5px}

  /* envelopes */
  .envelope{left:745px;width:410px;height:150px;overflow:hidden}
  .env-front{top:38px;height:166px;padding:16px 20px}
  .env-front .brand-dot{width:14px;height:14px}
  .env-front .brand-name{font-size:12px}
  .env-front .tagline{font-size:3.8px;margin:1px 0 0 18px}
  .env-front .watermark{position:absolute;right:26px;top:30px;width:90px;height:90px;border-radius:50%;background:var(--faint)}
  .env-front .footer-rule{position:absolute;left:0;right:0;bottom:8px;height:2px;background:var(--green)}
  .env-back-1{top:215px}
  .env-back-2{top:300px}
  .env-back-3{top:412px;height:205px}
  .envelope svg{position:absolute;left:0;top:0}
</style>
</head>
<body>

  <!-- business cards -->
  <p class="caption" style="left:57px;top:18px;width:98px">Business Card (Front)</p>
  <p class="caption" style="left:165px;top:18px;width:98px">Business Card (Back) Option 1</p>
  <p class="caption" style="left:275px;top:18px;width:98px">Business Card (Back) Option 2</p>
  <p class="caption" style="left:378px;top:18px;width:98px">Business Card (Back) Option 3</p>

  <section class="piece card card-front">
    <div class="brand"><span class="brand-dot"></span><span class="brand-name">Pebblewick Mortgages</span></div>
    <p class="tagline">Independent mortgage advice you can trust</p>
    <div class="person"><b>Owen Drisdale</b><br>Director</div>
    <div class="contact">T 01632 960418<br>M 07700 900412<br>owen@pebblewickmortgages.co.uk<br>www.pebblewickmortgages.co.uk</div>
    <div class="stripe"></div>
  </section>
  <section class="piece card card-back card-back-1"><span class="brand-dot"></span></section>
  <section class="piece card card-back card-back-2"><div class="brand"><span class="brand-dot"></span><span class="brand-name">Pebblewick Mortgages</span></div></section>
  <section class="piece card card-back card-back-3"><div class="brand"><span class="brand-dot"></span><span class="brand-name">Pebblewick Mortgages</span></div></section>

  <!-- fax -->
  <p class="caption" style="left:8px;top:86px;width:305px">The Fax</p>
  <section class="piece sheet fax">
    <div class="watermark"></div>
    <div class="brand"><span class="brand-dot"></span><span class="brand-name">Pebblewick Mortgages</span></div>
    <p class="tagline">Independent mortgage advice you can trust</p>
    <div class="address"><span>17-19 Marsh Lane<br>Fernby Hollow<br>LT4 7QW</span><span>T 01632 960418<br>owen@pebblewickmortgages.co.uk<br>www.pebblewickmortgages.co.uk</span></div>
    <p class="fax-title">FAX</p>
    <table class="fax-form">
      <tr><td class="label">To:</td><td></td><td class="label">From:</td><td></td></tr>
      <tr><td class="label">Fax:</td><td></td><td class="label">Pages:</td><td></td></tr>
      <tr><td class="label">Phone:</td><td></td><td class="label">Date:</td><td></td></tr>
      <tr><td class="label">Re:</td><td></td><td class="label">CC:</td><td></td></tr>
    </table>
    <div class="fax-checks"><span>Urgent</span><span>For Review</span><span>Please Comment</span><span>Please Reply</span><span>Please Recycle</span></div>
    <div class="footer-rule"></div>
  </section>

  <!-- letterhead -->
  <p class="caption" style="left:330px;top:86px;width:305px">Letterhead</p>
  <section class="piece sheet letterhead">
    <div class="watermark"></div>
    <div class="brand"><span class="brand-dot"></span><span class="brand-name">Pebblewick Mortgages</span></div>
    <p class="tagline">Independent mortgage advice you can trust</p>
    <div class="address"><span>17-19 Marsh Lane<br>Fernby Hollow<br>LT4 7QW</span><span>T 01632 960418<br>owen@pebblewickmortgages.co.uk<br>www.pebblewickmortgages.co.uk</span></div>
    <div class="footer-rule"></div>
  </section>

  <!-- envelopes -->
  <p class="caption" style="left:745px;top:27px;width:410px">Envelopes (Front)</p>
  <section class="piece envelope env-front">
    <div class="watermark"></div>
    <div class="brand"><span class="brand-dot"></span><span class="brand-name">Pebblewick Mortgages</span></div>
    <p class="tagline">Independent mortgage advice you can trust</p>
    <div class="footer-rule"></div>
  </section>

  <p class="caption" style="left:745px;top:206px;width:410px">Envelopes (Back) Option 1</p>
  <section class="piece envelope env-back-1">
    <svg width="410" height="150" viewBox="0 0 410 150">
      <polygon points="0,0 410,0 205,70" fill="#f4f4f4" stroke="#d8d8d8" stroke-width="0.8"/>
      <circle cx="205" cy="36" r="9" fill="var(--green)"/>
    </svg>
  </section>

  <section class="piece envelope env-back-2">
    <svg width="410" height="150" viewBox="0 0 410 150">
      <defs><linearGradient id="flapGreen" x1="0" y1="0" x2="0" y2="1"><stop offset="0" stop-color="#8cc63f"/><stop offset="1" stop-color="#2a6a17"/></linearGradient></defs>
      <polygon points="0,0 410,0 205,72" fill="url(#flapGreen)"/>
      <circle cx="205" cy="34" r="9" fill="#fff"/>
    </svg>
    <p class="caption" style="left:0;top:2px;width:410px;color:#fff">Envelopes (Back) Option 2</p>
  </section>

  <section class="piece envelope env-back-3">
    <svg width="410" height="205" viewBox="0 0 410 205">
      <defs><linearGradient id="flapLime" x1="0" y1="0" x2="0" y2="1"><stop offset="0" stop-color="#d6e05a"/><stop offset="1" stop-color="#9ab82a"/></linearGradient></defs>
      <polygon points="0,0 410,0 205,82" fill="url(#flapLime)"/>
      <circle cx="205" cy="42" r="9" fill="#fff"/>
    </svg>
    <p class="caption" style="left:0;top:6px;width:410px;color:#3d5a10">Envelopes (Back) Option 3</p>
  </section>

</body>
</html>
```